Book project Beatrix

I'm looking for a book cover idea and layout of the text for the chapter in part 1 and part 2.

I'm a dentist grew up in Sweden living in Chicago since 24 years. I've been working on a book for the past 4 years where I'm trying to convey the idea that your overall wellbeing is dependent on an holistic approach centered on your oral health. It all begins in the mouth!

I talk about my experiences and learnings as a Swedish -American, who has played professional golf, worked as a dentist in Sweden, researching mobile dental care (barriers to health), being a serial entrepreneur, including being the founder of BrightvaleForum, public health advocate, mother of 4, grandmother and wife.

In part 1 of the book I talk about the mouth and the mouth-body connection. Part 2 (the solutions) are 4 pillars, Eat, Sleep, Breathe and Move (your body and mind) for better overall wellbeing. I also hav a chapter about Habits. How to create your habits you want for success. Each pillar chapter ends with a worksheet for the reader to use to create new habits.

My style is more on the minimilist and simple less is more spectrum. I don't like clutter.. Most of my clothes are black - I use material to make outfits different. My home is black white and grey with an accent color of red.

I'm open minded that there are other choices than a black book.
My favorite book look is Petra Lindvoss's book

The title of the book is Lumo - a Nordic-rooted handbook for calm days that begins at your lips

Please play around with concepts of a mouth (think Velvet Harrows perhaps), using the O for mouth etc. I am looking for creative ideas that would make the book be attractive, stand out, create trials etc.

Target Market(s)

The health conscious person

Industry/Entity Type

wellness overall health

Font styles to use
Sans Serif

Colors

Designer to choose colors to be used in the design.

Requirements
Must have
• a book cover idea including titel and subtitel the swedish word MUNHÄLSA on the cover as well.
Nice to have
• book cover that draws the attention to mouth as the gateway
Should not have
• Color see upload file

```html
<!DOCTYPE html>
<html lang="en">
<head>
<meta charset="utf-8">
<title>Lumo – Book Cover</title>
<link rel="stylesheet" href="https://fonts.googleapis.com/css2?family=Oswald:wght@300;400;700&family=Montserrat:wght@400&display=swap">
<style>
  :root {
    --backdrop: #e4e4e4;
    --cover-yellow: #e9d203;
    --rule-yellow: #f3e260;
    --title-white: #f2f2f2;
    --accent-red: #e0161f;
    --ink: #151515;
    --photo-red: #d9242a;
    --photo-pink: #e59a92;
  }
  * { margin: 0; padding: 0; box-sizing: border-box; }
  html, body {
    width: 1200px;
    height: 800px;
    overflow: hidden;
    background: var(--backdrop);
  }
  .canvas {
    position: relative;
    width: 1200px;
    height: 800px;
  }
  .cover {
    position: absolute;
    left: 364px;
    top: 40px;
    width: 472px;
    height: 720px;
    background: var(--cover-yellow);
    text-align: center;
  }
  .cover__title {
    position: absolute;
    top: 10px;
    left: 0;
    width: 100%;
    font-family: "Oswald", sans-serif;
    font-weight: 700;
    font-size: 180px;
    line-height: 1;
    letter-spacing: -4px;
    color: var(--title-white);
    text-shadow: 0 2px 3px rgba(0, 0, 0, 0.18);
  }
  .cover__rule {
    position: absolute;
    left: 134px;
    width: 204px;
    height: 1px;
    background: var(--rule-yellow);
  }
  .cover__rule--top { top: 197px; }
  .cover__rule--bottom { top: 255px; }
  .cover__swedish {
    position: absolute;
    top: 211px;
    left: 0;
    width: 100%;
    font-family: "Montserrat", sans-serif;
    font-weight: 400;
    font-size: 29px;
    line-height: 1.2;
    letter-spacing: 0.5px;
    color: var(--accent-red);
  }
  .cover__photo {
    position: absolute;
    top: 276px;
    left: 78px;
    width: 316px;
    height: 254px;
    border-radius: 24px;
    background: radial-gradient(ellipse at 50% 55%, var(--photo-pink) 0%, var(--photo-red) 75%);
  }
  .cover__subtitle {
    position: absolute;
    top: 545px;
    left: 0;
    width: 100%;
    font-family: "Oswald", sans-serif;
    font-weight: 300;
    font-size: 24px;
    line-height: 30px;
    color: var(--ink);
  }
  .cover__author {
    position: absolute;
    top: 652px;
    left: 0;
    width: 100%;
    font-family: "Oswald", sans-serif;
    font-weight: 400;
    font-size: 28px;
    line-height: 1;
    letter-spacing: 8px;
    padding-left: 8px;
    color: var(--ink);
  }
</style>
</head>
<body>
  <main class="canvas">
    <section class="cover">
      <h1 class="cover__title">LUMO</h1>
      <div class="cover__rule cover__rule--top"></div>
      <p class="cover__swedish">MUNHÄLSA</p>
      <div class="cover__rule cover__rule--bottom"></div>

      <div class="cover__photo" role="img" aria-label="Photograph of an open mouth with red lips, white teeth and tongue out"></div>

      <p class="cover__subtitle">A Nordic-rooted handbook for calm days<br>that begins at your lips</p>
      <p class="cover__author">PROJECT BEATRIX</p>
    </section>
  </main>
</body>
</html>
```